Plumbing website that stands out

Seo optimized, mobile friendly, easily editable word press Plumbing website with google reviews widget. And widget of revolving photos of completed work. Contact page and services page, about page. Will provide, “About” content. And photos Need all other content written.
Services include:
Water heater replacement
Tankless water heater installation
Kitchen and bath remodel
Drain cleaning and clog removal
Leak repair
Faucet repair and replacement

I will be adding services and photos of recent completed projects as time goes on.

```html
<!DOCTYPE html>
<html lang="en">
<head>
<meta charset="utf-8">
<title>Clearline Plumbing</title>
<link rel="stylesheet" href="https://fonts.googleapis.com/css2?family=Cinzel:wght@500;600;700&family=Montserrat:wght@400;500;600;700&display=swap">
<style>
:root{
  --blue:#1f63ab;
  --navy:#1b4f8e;
  --deep:#1a4a86;
  --teal:#46bfd1;
  --hero:#4a86c8;
  --ink:#222a33;
  --muted:#555f6a;
  --line:#d9dee5;
  --gold:#f5b81c;
  --pale:#eef2f8;
  --grey:#e4e6ea;
}
*{box-sizing:border-box;margin:0;padding:0}
html,body{width:1200px;height:4938px;overflow:hidden}
body{font-family:"Montserrat",Arial,sans-serif;color:var(--ink);background:#fff;position:relative}
.btn{display:inline-flex;align-items:center;gap:14px;background:var(--blue);color:#fff;font-size:14px;font-weight:500;padding:0 20px;height:36px;border-radius:2px}
.btn svg{width:28px;height:10px}
.mark{width:46px;height:46px;background:var(--blue);margin:0 auto 12px}
.sec-title{font-family:"Cinzel",Georgia,serif;font-size:40px;font-weight:600;color:var(--blue);text-align:center;letter-spacing:1px}
.sec-sub{text-align:center;font-size:16px;color:var(--ink);margin-top:10px}

/* header + hero */
.hero{position:relative;height:860px;background:linear-gradient(180deg,#4d8acb 0%,#4680c2 100%);overflow:hidden}
.brand{position:absolute;left:0;top:0;width:360px;height:165px;background:#fff;border-bottom-right-radius:165px;display:flex;flex-direction:column;align-items:center;justify-content:center;padding-right:40px;z-index:3}
.brand .sq{width:54px;height:54px;background:var(--blue);margin-bottom:12px}
.brand .name{font-family:"Cinzel",Georgia,serif;font-weight:600;font-size:26px;color:var(--navy);letter-spacing:2px;text-align:center;line-height:1.1}
.topbar{position:absolute;left:320px;right:0;top:0;height:44px;background:var(--blue);display:flex;align-items:center;justify-content:flex-end;padding-right:60px;gap:10px;color:#fff;font-size:14px}
.topbar b{font-weight:700}
.topbar .ic{width:18px;height:18px}
.social{display:flex;gap:8px;margin-left:12px}
.social i{width:22px;height:22px;border-radius:50%;background:#fff;display:block}
.nav{position:absolute;left:320px;right:0;top:44px;height:70px;background:var(--teal);display:flex;align-items:center;padding-left:100px;gap:48px;color:#fff;font-size:15px;font-weight:500}
.hero h1{position:absolute;top:230px;left:0;right:0;text-align:center;font-family:"Cinzel",Georgia,serif;font-weight:500;font-size:70px;line-height:78px;color:#fff;letter-spacing:2px}
.hero .btn{position:absolute;top:418px;left:50%;transform:translateX(-50%);height:54px;padding:0 28px;font-size:17px;background:var(--deep)}
.arrow-c{position:absolute;width:42px;height:42px;border:2px solid #fff;border-radius:50%}
.arrow-c svg{width:100%;height:100%}
.tools{position:absolute;left:0;right:0;bottom:0;height:280px;background:linear-gradient(180deg,rgba(74,134,200,0) 0%,#7b8fa6 45%,#9aa7b6 100%)}

/* about */
.about{position:relative;height:680px;display:flex;align-items:flex-start;padding:70px 85px 0}
.about .art{width:320px;height:340px;background:linear-gradient(135deg,#1f5fa5 0%,#2e7bbf 55%,#46bfd1 100%);flex:none}
.about .divider{width:1px;height:360px;background:var(--line);margin:0 40px}
.about .txt{width:500px;padding-top:4px}
.about h2{font-family:"Cinzel",Georgia,serif;font-weight:600;font-size:30px;color:var(--blue);line-height:1}
.about h3{font-family:"Cinzel",Georgia,serif;font-weight:500;font-size:28px;color:var(--ink);margin-top:6px}
.about p{font-size:12px;line-height:16.5px;text-align:justify;margin-top:18px;color:#333}
.about .btn{margin-top:22px}

/* services */
.services{position:relative;height:820px;background:linear-gradient(180deg,#dde6f2 0%,#f4f7fb 70%,#fff 100%)}
.services .curve{position:absolute;top:-60px;left:0;width:1200px;height:120px}
.services .head{position:absolute;top:20px;left:0;right:0}
.svc-row{position:absolute;top:240px;left:150px;right:150px;display:flex;justify-content:space-between}
.svc{width:190px;text-align:center}
.svc .photo{width:180px;height:180px;border-radius:50%;margin:0 auto;background:radial-gradient(circle at 50% 40%,#f5f6f8 0%,#c9ced6 100%);border:4px solid #fff;box-shadow:0 2px 6px rgba(0,0,0,.12);position:relative}
.svc .badge{width:56px;height:56px;border-radius:50%;background:var(--teal);border:4px solid #fff;margin:-38px auto 0;position:relative}
.svc .badge svg{width:100%;height:100%}
.svc h4{font-size:18px;font-weight:500;line-height:24px;margin-top:14px;height:48px}
.svc .btn{margin-top:22px;height:34px;font-size:13px}
.chev{position:absolute;top:320px;width:24px;height:24px}

/* recent work */
.recent{position:relative;height:960px;background:var(--grey)}
.recent .wave{position:absolute;left:0;width:1200px;height:110px}
.recent .head{position:absolute;top:70px;left:0;right:0}
.grid{position:absolute;top:260px;left:150px;display:grid;grid-template-columns:440px 214px 214px;grid-template-rows:214px 214px;gap:12px}
.grid .ph{background:linear-gradient(135deg,#9aa4ae,#d7dbe0)}
.grid .big{grid-row:1/3}
.grid .over{background:#3a78bd;display:flex;align-items:center;justify-content:center}
.grid .over svg{width:46px;height:46px}
.recent .btn{position:absolute;top:718px;left:50%;transform:translateX(-50%);height:34px;font-size:13px}

/* reviews */
.reviews{position:relative;height:700px}
.reviews .head{position:absolute;top:80px;left:0;right:0}
.cards{position:absolute;top:290px;left:175px;display:flex;gap:34px}
.card{width:262px;height:260px;background:#fff;box-shadow:0 2px 10px rgba(0,0,0,.14);border-radius:6px;padding:24px 22px;text-align:center}
.card.active{background:var(--blue);color:#fff}
.stars{color:var(--gold);font-size:22px;letter-spacing:3px}
.card p{font-size:12px;line-height:17px;margin-top:14px;height:108px}
.card .rule{border-top:1px dashed #aab3bd;margin:10px 0 12px}
.card.active .rule{border-color:rgba(255,255,255,.5)}
.card h5{font-size:15px;font-weight:700;color:var(--blue)}
.card.active h5{color:#fff}
.reviews .arrow-c{top:400px;border-color:var(--teal)}

/* contact */
.contact{position:absolute;top:4060px;left:188px;width:824px;height:420px;display:flex;z-index:2;box-shadow:0 4px 14px rgba(0,0,0,.15)}
.form{flex:1;background:#fff;padding:30px 26px}
.form h2,.details h2{font-family:"Cinzel",Georgia,serif;font-weight:600;font-size:32px}
.form h2{color:var(--blue)}
.fields{display:grid;grid-template-columns:1fr 1fr;gap:12px;margin-top:26px}
.field{height:36px;border:1px solid #c9ced6;font-size:10px;color:#888;padding:12px 10px}
.field.msg{grid-column:1/3;height:110px}
.send{height:36px;background:var(--teal);color:#fff;font-size:11px;font-weight:600;display:flex;align-items:center;justify-content:center;margin-top:12px;letter-spacing:1px}
.details{width:340px;background:var(--navy);color:#fff;padding:30px 22px}
.details h2{font-size:30px}
.drow{display:flex;align-items:center;gap:12px;padding:16px 0;border-bottom:1px solid rgba(255,255,255,.25);font-size:13px;line-height:18px}
.drow .ci{width:30px;height:30px;border-radius:50%;background:#fff;flex:none}
.drow .ci svg{width:30px;height:30px}
.drow.big{font-size:20px;font-weight:500}
.drow.soc{border:none;gap:8px;font-size:13px}
.drow.soc i{width:22px;height:22px;border-radius:50%;background:#fff;display:block;margin-left:10px}
.drow.soc i:first-child{margin-left:0}

/* footer */
.footer{position:absolute;left:0;right:0;top:4380px;bottom:0;background:linear-gradient(180deg,#1f5aa0 0%,#1a4a86 100%);color:#fff}
.footer .fbrand{position:absolute;left:130px;top:190px;display:flex;flex-direction:column;align-items:center}
.footer .fbrand .sq{width:60px;height:60px;background:#fff;margin-bottom:16px}
.footer .fbrand .name{font-family:"Cinzel",Georgia,serif;font-weight:600;font-size:30px;letter-spacing:2px;color:#fff;text-align:center;line-height:1.1}
.fnav{position:absolute;left:530px;top:200px;display:flex;gap:30px;font-size:15px;font-weight:500}
.footer .rule{position:absolute;left:470px;right:130px;top:250px;height:1px;background:rgba(255,255,255,.25)}
.copy{position:absolute;right:130px;top:278px;font-size:12px}
</style>
</head>
<body>

<section class="hero">
  <div class="brand">
    <div class="sq"></div>
    <div class="name">CLEARLINE<br>PLUMBING</div>
  </div>
  <div class="topbar">
    <svg class="ic" viewBox="0 0 20 20"><circle cx="10" cy="10" r="10" fill="#fff"/><path d="M6.5 5.5l2 0 1 2.6-1.3 1a6 6 0 0 0 3 3l1-1.3 2.6 1 0 2a1 1 0 0 1-1 1A9 9 0 0 1 5.5 6.5a1 1 0 0 1 1-1z" fill="#1f63ab"/></svg>
    <span><b>Call us:</b> (555) 014-2286 |</span>
    <svg class="ic" viewBox="0 0 20 20"><circle cx="10" cy="10" r="10" fill="#fff"/><rect x="5" y="6.5" width="10" height="7" fill="#1f63ab"/><path d="M5 6.5l5 4 5-4" stroke="#fff" fill="none"/></svg>
    <span><b>Email us:</b> info@clearlineplumbing.com</span>
    <div class="social"><i></i><i></i><i></i></div>
  </div>
  <nav class="nav"><span>Home Page</span><span>About Us</span><span>Our Services</span><span>Recent Work</span><span>Contact us</span></nav>

  <h1>WELCOME TO<br>CLEARLINE PLUMBING</h1>
  <div class="btn">Contact Us <svg viewBox="0 0 28 10"><path d="M0 5h20" stroke="#fff" stroke-dasharray="2 2"/><path d="M20 1l5 4-5 4" stroke="#fff" fill="none"/><path d="M27 1v8" stroke="#fff"/></svg></div>
  <div class="arrow-c" style="left:100px;top:540px"><svg viewBox="0 0 42 42"><path d="M24 13l-8 8 8 8" stroke="#fff" stroke-width="2" fill="none"/></svg></div>
  <div class="arrow-c" style="right:100px;top:540px"><svg viewBox="0 0 42 42"><path d="M18 13l8 8-8 8" stroke="#fff" stroke-width="2" fill="none"/></svg></div>
  <div class="tools" role="img" aria-label="Photo of plumbing tools, wrenches, fittings and hoses laid out on a blue surface"></div>
</section>

<section class="about">
  <div class="art" role="img" aria-label="Brand illustration of a figure pouring water from a jug"></div>
  <div class="divider"></div>
  <div class="txt">
    <h2>ABOUT US</h2>
    <h3>CLEARLINE PLUMBING</h3>
    <p>Lorem Ipsum is simply dummy text of the printing and typesetting industry. Lorem Ipsum has been the industry's standard dummy text ever since the 1500s, when an unknown printer took a galley of type and scrambled it to make a type specimen book. It has survived not only five centuries, but also the leap into electronic typesetting, remaining essentially unchanged. It was popularised in the 1960s with the release of transfer sheets containing Lorem Ipsum passages, and more recently with desktop publishing software like common page layout tools including versions of Lorem Ipsum.</p>
    <p>Lorem Ipsum is simply dummy text of the printing and typesetting industry. Lorem Ipsum has been the industry's standard dummy text ever since the 1500s, when an unknown printer took a galley of type and scrambled it to make a type specimen book. It has survived not only five centuries, but also the leap into electronic typesetting.</p>
    <div class="btn">Read More <svg viewBox="0 0 28 10"><path d="M0 5h20" stroke="#fff" stroke-dasharray="2 2"/><path d="M20 1l5 4-5 4" stroke="#fff" fill="none"/><path d="M27 1v8" stroke="#fff"/></svg></div>
  </div>
</section>

<section class="services">
  <svg class="curve" viewBox="0 0 1200 120" preserveAspectRatio="none"><path d="M0 120 Q600 0 1200 120Z" fill="#dde6f2"/></svg>
  <div class="head">
    <div class="mark"></div>
    <div class="sec-title">OUR SERVICES</div>
    <div class="sec-sub">Lorem Ipsum is simply dummy text of the printing and typesetting industry.</div>
  </div>
  <svg class="chev" style="left:98px" viewBox="0 0 24 24"><path d="M16 3l-9 9 9 9" stroke="#9aa4ae" stroke-width="2" fill="none"/></svg>
  <svg class="chev" style="right:98px" viewBox="0 0 24 24"><path d="M8 3l9 9-9 9" stroke="#9aa4ae" stroke-width="2" fill="none"/></svg>
  <div class="svc-row">
    <div class="svc">
      <div class="photo" role="img" aria-label="Photo of a technician servicing a water heater"></div>
      <div class="badge"><svg viewBox="0 0 56 56"><rect x="20" y="16" width="16" height="24" rx="3" fill="#fff"/></svg></div>
      <h4>Water heater<br>replacement</h4>
      <div class="btn">More Info <svg viewBox="0 0 28 10"><path d="M0 5h20" stroke="#fff" stroke-dasharray="2 2"/><path d="M20 1l5 4-5 4" stroke="#fff" fill="none"/><path d="M27 1v8" stroke="#fff"/></svg></div>
    </div>
    <div class="svc">
      <div class="photo" role="img" aria-label="Photo of a wall-mounted tankless water heater"></div>
      <div class="badge"><svg viewBox="0 0 56 56"><rect x="19" y="15" width="18" height="26" rx="2" fill="#fff"/></svg></div>
      <h4>Tankless water<br>heater installation</h4>
      <div class="btn">More Info <svg viewBox="0 0 28 10"><path d="M0 5h20" stroke="#fff" stroke-dasharray="2 2"/><path d="M20 1l5 4-5 4" stroke="#fff" fill="none"/><path d="M27 1v8" stroke="#fff"/></svg></div>
    </div>
    <div class="svc">
      <div class="photo" role="img" aria-label="Photo of a modern kitchen faucet over a sink"></div>
      <div class="badge"><svg viewBox="0 0 56 56"><rect x="16" y="22" width="24" height="16" fill="#fff"/><path d="M24 22v-6h8" stroke="#fff" stroke-width="2" fill="none"/></svg></div>
      <h4>Kitchen and<br>bath remodel</h4>
      <div class="btn">More Info <svg viewBox="0 0 28 10"><path d="M0 5h20" stroke="#fff" stroke-dasharray="2 2"/><path d="M20 1l5 4-5 4" stroke="#fff" fill="none"/><path d="M27 1v8" stroke="#fff"/></svg></div>
    </div>
    <div class="svc">
      <div class="photo" role="img" aria-label="Photo of a plumber clearing a drain pipe"></div>
      <div class="badge"><svg viewBox="0 0 56 56"><path d="M18 18v12a6 6 0 0 0 12 0v-4h8" stroke="#fff" stroke-width="5" fill="none"/></svg></div>
      <h4>Drain cleaning<br>and clog removal</h4>
      <div class="btn">More Info <svg viewBox="0 0 28 10"><path d="M0 5h20" stroke="#fff" stroke-dasharray="2 2"/><path d="M20 1l5 4-5 4" stroke="#fff" fill="none"/><path d="M27 1v8" stroke="#fff"/></svg></div>
    </div>
  </div>
</section>

<section class="recent">
  <svg class="wave" style="top:-50px" viewBox="0 0 1200 110" preserveAspectRatio="none"><path d="M0 110 Q600 -20 1200 110Z" fill="#e4e6ea"/><path d="M0 110 Q600 -20 1200 110" stroke="#46bfd1" stroke-width="10" fill="none"/></svg>
  <div class="head">
    <div class="mark"></div>
    <div class="sec-title">RECENT WORK</div>
    <div class="sec-sub">Lorem Ipsum is simply dummy text of the printing and typesetting industry.</div>
  </div>
  <div class="grid">
    <div class="ph big" role="img" aria-label="Photo of a hand tightening a chrome sink trap with a red wrench"></div>
    <div class="ph" role="img" aria-label="Photo of a plumber working under a sink"></div>
    <div class="ph" style="background:linear-gradient(135deg,#2b3035,#6b7177)" role="img" aria-label="Photo of stacked black corrugated drain pipes"></div>
    <div class="over" role="img" aria-label="Photo of plumbing tools with a blue highlight overlay"><svg viewBox="0 0 46 46"><circle cx="23" cy="23" r="23" fill="#fff"/><circle cx="21" cy="21" r="8" stroke="#46bfd1" stroke-width="2.5" fill="none"/><path d="M27 27l6 6" stroke="#46bfd1" stroke-width="2.5"/><path d="M17 21h8M21 17v8" stroke="#46bfd1" stroke-width="2"/></svg></div>
    <div class="ph" role="img" aria-label="Photo of brass water meters with connected hoses"></div>
  </div>
  <div class="btn">Read More <svg viewBox="0 0 28 10"><path d="M0 5h20" stroke="#fff" stroke-dasharray="2 2"/><path d="M20 1l5 4-5 4" stroke="#fff" fill="none"/><path d="M27 1v8" stroke="#fff"/></svg></div>
  <svg class="wave" style="bottom:0" viewBox="0 0 1200 110" preserveAspectRatio="none"><path d="M0 0 Q600 130 1200 0V110H0Z" fill="#fff"/><path d="M0 0 Q600 130 1200 0" stroke="#46bfd1" stroke-width="10" fill="none"/></svg>
</section>

<section class="reviews">
  <div class="head">
    <div class="mark"></div>
    <div class="sec-title">CUSTOMER REVIEWS</div>
    <div class="sec-sub">Lorem Ipsum is simply dummy text of the printing and typesetting industry.</div>
  </div>
  <div class="arrow-c" style="left:108px"><svg viewBox="0 0 42 42"><path d="M24 13l-8 8 8 8" stroke="#46bfd1" stroke-width="2" fill="none"/></svg></div>
  <div class="arrow-c" style="right:108px"><svg viewBox="0 0 42 42"><path d="M18 13l8 8-8 8" stroke="#46bfd1" stroke-width="2" fill="none"/></svg></div>
  <div class="cards">
    <div class="card"><div class="stars">★★★★★</div><p>“Lorem Ipsum is simply dummy text of the printing and typesetting industry. Lorem Ipsum has been the industry's standard dummy text ever since the 1500s, when an unknown printer took a galley”</p><div class="rule"></div><h5>Nora Whitfield</h5></div>
    <div class="card active"><div class="stars">★★★★★</div><p>“Lorem Ipsum is simply dummy text of the printing and typesetting industry. Lorem Ipsum has been the industry's standard dummy text ever since the 1500s, when an unknown printer took a galley”</p><div class="rule"></div><h5>Dale Corbin</h5></div>
    <div class="card"><div class="stars">★★★★★</div><p>“Lorem Ipsum is simply dummy text of the printing and typesetting industry. Lorem Ipsum has been the industry's standard dummy text ever since the 1500s, when an unknown printer took a galley”</p><div class="rule"></div><h5>Ray Okafor</h5></div>
  </div>
</section>

<section class="contact">
  <div class="form">
    <h2>CONTACT US</h2>
    <div class="fields">
      <div class="field">FIRST NAME*</div>
      <div class="field">LAST NAME*</div>
      <div class="field">E-MAIL*</div>
      <div class="field">PHONE*</div>
      <div class="field msg">MESSAGE</div>
    </div>
    <div class="send">SEND NOW</div>
  </div>
  <div class="details">
    <h2>CONTACT DETAILS</h2>
    <div class="drow"><span class="ci"><svg viewBox="0 0 30 30"><path d="M15 7a5 5 0 0 1 5 5c0 4-5 10-5 10s-5-6-5-10a5 5 0 0 1 5-5z" fill="#1b4f8e"/><circle cx="15" cy="12" r="2" fill="#fff"/></svg></span><span>1234 Sample Parkway,<br>Riverside Corners, GA 30092</span></div>
    <div class="drow big"><span class="ci"><svg viewBox="0 0 30 30"><path d="M10 8l3 0 1.5 3.8-2 1.5a9 9 0 0 0 4.2 4.2l1.5-2 3.8 1.5 0 3a1.5 1.5 0 0 1-1.5 1.5A13 13 0 0 1 8.5 9.5 1.5 1.5 0 0 1 10 8z" fill="#1b4f8e"/></svg></span><span>(555) 014-2286</span></div>
    <div class="drow"><span class="ci"><svg viewBox="0 0 30 30"><rect x="8" y="10" width="14" height="10" fill="#1b4f8e"/><path d="M8 10l7 6 7-6" stroke="#fff" fill="none"/></svg></span><span>hello@clearlineplumbing.com</span></div>
    <div class="drow soc"><i></i><span>Friendbook</span><i></i><span>Chirper</span><i></i><span>Linkwork</span></div>
  </div>
</section>

<footer class="footer">
  <div class="fbrand"><div class="sq"></div><div class="name">CLEARLINE<br>PLUMBING</div></div>
  <nav class="fnav"><span>Home</span><span>About Us</span><span>Our Services</span><span>Recent Work</span><span>Contact us</span></nav>
  <div class="rule"></div>
  <div class="copy">Copyright © 2022 Clearline Plumbing | All Right Reserved</div>
</footer>

</body>
</html>
```